RidgeHornSupply.com

I need a new webdesign for a company in the San Jose/SF Bay area that showcases the financial benefits of buying used band instruments for junior high students.This would be opposed to the current and costly option of renting cheap quality instruments from the 2 or 3 local music stores that charge a monthly fee that over the years charges the buyer 3 or 4x over..
Instruments: focus in on Alto Sax, Trumpet, Flute, Clarinet, Trombone, Tenor Sax, Baritone
Target middle schools are Kestrelwood Middle School and Harlow Middle School in San Jose, CA. Both have award winning band programs.
Files attached may or may not be important.
Tabs Needed and funtional
Contact
Shopping Cart
Select Instrument
Checkout
Add to Cart, etc.
Instuments
quantity, etc.
trade in your instrument/sell your instrument
ability to add or take away new instruments for sale. including pictures
Additional questions or info, feel free to ask
Hi Designers,
Project Deadline Extended
Reason: In the next week you will be receiving specific content that will be required to be had on the website.
New desigins are still welcome. Please continue to contact me if you have questions about your individual designs.
Thanks!
Ridge Horn

```html
<!DOCTYPE html>
<html lang="en">
<head>
<meta charset="utf-8">
<title>Ridge Horn Instruments</title>
<link href="https://fonts.googleapis.com/css2?family=Open+Sans:wght@400;600;700&display=swap" rel="stylesheet">
<style>
:root{
  --red:#d0121b;
  --red-dark:#b50d15;
  --green:#4aa321;
  --green-dark:#3d8c1a;
  --ink:#222;
  --text:#555;
  --muted:#888;
  --line:#dcdcdc;
  --page:#f4f4f4;
  --card:#fff;
  --footer:#3f3f3f;
  --footer-bar:#2f2f2f;
  --footer-text:#cfcfcf;
}
*{box-sizing:border-box;margin:0;padding:0}
html,body{width:1034px;height:1200px;overflow:hidden}
body{background:var(--page);font-family:"Open Sans",Arial,sans-serif;color:var(--text);font-size:11px}
.wrap{width:844px;margin-left:95px;position:relative}
a{color:inherit;text-decoration:none}

/* header */
.site-header{height:88px;position:relative}
.brand{position:absolute;left:0;top:13px;display:flex;align-items:center;gap:8px}
.brand-mark{width:50px;height:50px;border-radius:50%;background:var(--red)}
.brand-name{font-size:21px;font-weight:700;color:var(--ink);line-height:1.05;text-transform:uppercase;letter-spacing:.5px}
.top-links{position:absolute;right:0;top:9px;display:flex;gap:14px;font-size:10px;color:var(--muted)}
.top-link{display:flex;align-items:center;gap:6px;line-height:1.2}
.top-link small{display:block;font-size:8.5px}
.icon-dot{width:17px;height:17px;border-radius:50%;background:var(--green);display:flex;align-items:center;justify-content:center}
.account-bar{position:absolute;right:0;top:55px;display:flex;align-items:center;gap:8px;border-top:1px solid var(--line);padding-top:0}
.my-account{display:flex;align-items:center;gap:5px;font-size:10.5px;color:var(--muted)}
.search{width:149px;height:22px;border:1px solid var(--line);background:#fff;display:flex;align-items:center;justify-content:space-between;padding:0 6px;font-size:9.5px;color:var(--muted)}
.cart{display:flex;height:22px}
.cart-icon{width:30px;background:var(--red);display:flex;align-items:center;justify-content:center}
.cart-total{background:#bfe3a8;color:#3a6b21;padding:0 5px;font-size:10.5px;line-height:22px}

/* nav */
.main-nav{height:33px;background:linear-gradient(#e0161f,var(--red-dark));border-radius:3px;display:flex;overflow:hidden}
.main-nav a{color:#fff;font-weight:700;font-size:11.5px;line-height:33px;padding:0 10.3px;text-transform:uppercase}
.main-nav a.active{background:var(--green);padding:0 13px}

/* hero */
.hero{margin-top:5px;height:310px;position:relative;overflow:hidden;border-radius:3px 3px 0 0}
.hero-photo{position:absolute;inset:0;background:linear-gradient(100deg,#d9cbb5 0%,#b7a58d 30%,#6d7c98 50%,#c9b9a3 70%,#d66a2a 92%)}
.hero-curve{position:absolute;left:0;bottom:0;width:844px;height:70px}
.hero-caption{position:absolute;left:0;top:121px;width:296px;height:133px;background:rgba(255,255,255,.82);padding:13px 28px}
.hero-caption h1{font-size:26px;font-weight:700;color:#111;line-height:1.1}
.hero-caption p{font-size:12.5px;color:#444;margin-top:5px;line-height:1.35}
.btn-hero{display:inline-block;margin-top:11px;background:var(--red);color:#fff;font-weight:700;font-size:13px;padding:0 25px;line-height:31px}

/* section titles */
.section-title{position:relative;text-align:center;height:20px}
.section-title::before{content:"";position:absolute;left:0;right:0;top:9px;height:4px;border-top:1px solid var(--line);border-bottom:1px solid var(--line)}
.section-title span{position:relative;background:var(--page);padding:0 10px;font-size:15px;font-weight:600;color:var(--ink);text-transform:uppercase}

/* products */
.featured{margin-top:13px}
.products{margin-top:9px;display:grid;grid-template-columns:repeat(4,203px);gap:11px;position:relative}
.product{height:244px;background:linear-gradient(#fff 60%,#f1f1f1);border:1px solid var(--line);border-radius:2px;position:relative;overflow:hidden;text-align:center}
.product-photo{width:140px;height:110px;margin:22px auto 0;border-radius:4px}
.photo-sax{background:linear-gradient(135deg,#f6dede,#e3474b 50%,#f6dede)}
.photo-trumpet{background:linear-gradient(135deg,#f7f0d6,#c9a63a 50%,#f7f0d6)}
.photo-flute{background:linear-gradient(135deg,#fbeee0,#ec7a2a 50%,#eaf3f8)}
.photo-clarinet{background:linear-gradient(135deg,#f0f0f0,#3a3a3a 50%,#f0f0f0)}
.sale-ribbon{position:absolute;left:-26px;top:14px;width:110px;transform:rotate(-45deg);background:#3a3a3a;color:#fff;font-size:10px;font-weight:700;line-height:20px}
.product h3{margin-top:26px;font-size:12px;font-weight:700;color:var(--ink)}
.price{font-size:12px;color:var(--ink);margin-top:4px}
.price b{color:var(--red);font-weight:400}
.product-actions{display:flex;justify-content:center;gap:10px;margin-top:19px}
.btn{display:inline-block;width:82px;line-height:24px;color:#fff;font-size:10.5px;border-radius:2px;text-transform:uppercase}
.btn-red{background:var(--red)}
.btn-green{background:var(--green)}
.slider-arrow{position:absolute;top:111px;width:21px;height:21px;border-radius:50%;background:#3a3a3a;display:flex;align-items:center;justify-content:center}
.slider-arrow.prev{left:-35px}
.slider-arrow.next{right:-35px}

/* testimonials */
.testimonials{margin-top:14px}
.two-col{margin-top:10px;display:grid;grid-template-columns:414px 414px;gap:16px}
.panel{background:linear-gradient(#fff 60%,#f1f1f1);border:1px solid var(--line);border-radius:2px}
.quote{height:104px;padding:18px 20px 0 33px;position:relative;font-size:10.5px;line-height:1.66}
.quote-mark{position:absolute;left:14px;top:2px;font-size:58px;color:#ddd;font-family:Georgia,serif;line-height:1}
.quote p{position:relative}
.quote cite{font-weight:700;font-style:italic;color:#444;margin-left:4px}

/* payments */
.payments{margin-top:20px}
.payments .two-col{margin-top:9px}
.box{height:104px;padding:14px 20px}
.box h4{font-size:13px;font-weight:600;color:var(--ink);text-transform:uppercase}
.box p{font-size:10.5px;color:#444;margin-top:6px}
.signup{display:flex;gap:7px;margin-top:13px}
.signup-input{width:180px;height:27px;border:1px solid #ccc;border-radius:3px;background:#fff}
.btn-dark{background:#3a3a3a;color:#fff;font-size:10px;font-weight:700;padding:0 10px;line-height:27px;border-radius:3px}
.cards{display:flex;gap:9px;margin-top:11px}
.card-chip{width:45px;height:26px;background:#fff;border:1px solid #e2e2e2;box-shadow:0 1px 2px rgba(0,0,0,.15);font-size:7.5px;font-weight:600;color:#555;display:flex;align-items:center;justify-content:center;text-align:center;line-height:1}

/* footer */
.site-footer{position:absolute;left:0;top:1023px;width:1034px;height:177px;background:var(--footer)}
.footer-cols{position:relative;height:150px}
.footer-col{position:absolute;top:17px}
.footer-col h5{font-size:12px;font-weight:700;color:#fff;margin-bottom:10px}
.footer-col ul{list-style:none;font-size:10.5px;color:var(--footer-text);line-height:19.8px}
.social li{display:flex;align-items:center;gap:10px;height:31px;color:#fff}
.social-dot{width:27px;height:27px;border-radius:50%;background:#d8d8d8}
.footer-bar{position:absolute;left:0;bottom:0;width:100%;height:27px;background:var(--footer-bar);text-align:center;font-size:8.5px;color:#aaa;line-height:27px}
</style>
</head>
<body>
<div class="wrap">
  <header class="site-header">
    <a class="brand" href="#">
      <span class="brand-mark"></span>
      <span class="brand-name">Ridge Horn<br>Instruments</span>
    </a>
    <div class="top-links">
      <div class="top-link"><span class="icon-dot"><svg width="10" height="8" viewBox="0 0 10 8"><rect x="0" y="1" width="6" height="5" fill="#fff"/><rect x="6" y="3" width="3" height="3" fill="#fff"/></svg></span>Shipping</div>
      <div class="top-link"><span class="icon-dot"><svg width="10" height="10" viewBox="0 0 10 10"><path d="M2 1l2 2-1 1c1 1.5 2 2.5 3 3l1-1 2 2-1.5 1.5C4 9 1 6 .5 2.5z" fill="#fff"/></svg></span><span>Customer Hotline<small>1-555-014-2290</small></span></div>
      <div class="top-link"><span class="icon-dot"><svg width="8" height="10" viewBox="0 0 8 10"><path d="M4 0a4 4 0 0 1 4 4c0 3-4 6-4 6S0 7 0 4a4 4 0 0 1 4-4z" fill="#fff"/><circle cx="4" cy="4" r="1.5" fill="#4aa321"/></svg></span><span>Store<br>Locations</span></div>
    </div>
    <div class="account-bar">
      <span class="my-account"><svg width="15" height="15" viewBox="0 0 15 15"><circle cx="7.5" cy="7.5" r="7" fill="none" stroke="#999"/><circle cx="7.5" cy="6" r="2.4" fill="none" stroke="#999"/><path d="M3 12c1.5-3 7.5-3 9 0" fill="none" stroke="#999"/></svg>My Account</span>
      <span class="search">Search<svg width="12" height="12" viewBox="0 0 12 12"><circle cx="5" cy="5" r="3.8" fill="none" stroke="#555" stroke-width="1.6"/><path d="M8 8l3 3" stroke="#555" stroke-width="1.8"/></svg></span>
      <span class="cart"><span class="cart-icon"><svg width="16" height="14" viewBox="0 0 16 14"><path d="M1 1h3l2 8h8l1.5-6H5" fill="none" stroke="#fff" stroke-width="1.6"/><circle cx="7" cy="12" r="1.3" fill="#fff"/><circle cx="13" cy="12" r="1.3" fill="#fff"/></svg></span><span class="cart-total">0 items: $0.00</span></span>
    </div>
  </header>

  <nav class="main-nav">
    <a class="active" href="#">Home</a>
    <a href="#">About Us</a>
    <a href="#">Products</a>
    <a href="#">Sale</a>
    <a href="#">Select Instrument</a>
    <a href="#">Instuments</a>
    <a href="#">Quantity</a>
    <a href="#">Contact Us</a>
  </nav>

  <section class="hero">
    <div class="hero-photo" role="img" aria-label="Young students playing brass and woodwind instruments together"></div>
    <svg class="hero-curve" viewBox="0 0 844 70" preserveAspectRatio="none">
      <path d="M0 0 Q422 100 844 0 L844 70 L0 70 Z" fill="#f4f4f4"/>
      <path d="M0 0 Q422 100 844 0" fill="none" stroke="#4aa321" stroke-width="5"/>
    </svg>
    <div class="hero-caption">
      <h1>BAND INSTRUMENTS</h1>
      <p>Lorem Ipsum is simply dummy text of the printing and typesetting industry</p>
      <a class="btn-hero" href="#">DETAILS</a>
    </div>
  </section>

  <section class="featured">
    <div class="section-title"><span>Featured Products</span></div>
    <div class="products">
      <a class="slider-arrow prev" href="#"><svg width="6" height="7" viewBox="0 0 6 7"><path d="M5 0v7L0 3.5z" fill="#fff"/></svg></a>
      <article class="product">
        <div class="product-photo photo-sax" role="img" aria-label="Red alto sax"></div>
        <h3>ALTO SAX</h3>
        <p class="price">PRICE: <b>$20,00</b></p>
        <div class="product-actions"><a class="btn btn-red" href="#">Deatil</a><a class="btn btn-green" href="#">Add to Cart</a></div>
      </article>
      <article class="product">
        <span class="sale-ribbon">SALE</span>
        <div class="product-photo photo-trumpet" role="img" aria-label="Brass trumpet"></div>
        <h3>TRUMPET</h3>
        <p class="price">PRICE: <b>$20,00</b></p>
        <div class="product-actions"><a class="btn btn-red" href="#">Deatil</a><a class="btn btn-green" href="#">Add to Cart</a></div>
      </article>
      <article class="product">
        <div class="product-photo photo-flute" role="img" aria-label="Orange flute"></div>
        <h3>FLUTE</h3>
        <p class="price">PRICE: <b>$20,00</b></p>
        <div class="product-actions"><a class="btn btn-red" href="#">Deatil</a><a class="btn btn-green" href="#">Add to Cart</a></div>
      </article>
      <article class="product">
        <div class="product-photo photo-clarinet" role="img" aria-label="Black clarinet"></div>
        <h3>CLARINET</h3>
        <p class="price">PRICE: <b>$20,00</b></p>
        <div class="product-actions"><a class="btn btn-red" href="#">Deatil</a><a class="btn btn-green" href="#">Add to Cart</a></div>
      </article>
      <a class="slider-arrow next" href="#"><svg width="6" height="7" viewBox="0 0 6 7"><path d="M1 0v7L6 3.5z" fill="#fff"/></svg></a>
    </div>
  </section>

  <section class="testimonials">
    <div class="section-title"><span>Testimonials</span></div>
    <div class="two-col">
      <blockquote class="panel quote"><span class="quote-mark">&ldquo;</span><p>Lorem Ipsum is simply dummy text of the printing and typesetting industry. Lorem Ipsum has been the industry's standard dummy text ever since the 1500s, when an unknown printer took a galley of type and scrambled it to make a type specimen book. <cite>Mara Ellison</cite></p></blockquote>
      <blockquote class="panel quote"><span class="quote-mark">&ldquo;</span><p>Lorem Ipsum is simply dummy text of the printing and typesetting industry. Lorem Ipsum has been the industry's standard dummy text ever since the 1500s, when an unknown printer took a galley of type and scrambled it to make a type specimen book. <cite>Mara Ellison</cite></p></blockquote>
    </div>
  </section>

  <section class="payments">
    <div class="section-title"><span>Payments</span></div>
    <div class="two-col">
      <div class="panel box">
        <h4>Newsletter Signup</h4>
        <p>Lorem Ipsum is simply dummy text of the printing and typesetting industry.</p>
        <div class="signup"><span class="signup-input"></span><a class="btn-dark" href="#">SUBSCRIBE</a></div>
      </div>
      <div class="panel box">
        <h4>Payment Method</h4>
        <p>Lorem Ipsum is simply dummy text of the printing and typesetting industry.</p>
        <div class="cards">
          <span class="card-chip">Veltra</span>
          <span class="card-chip">Cardly</span>
          <span class="card-chip">Kobu</span>
          <span class="card-chip">PayNest</span>
          <span class="card-chip">Findr</span>
          <span class="card-chip">Transit Pay</span>
        </div>
      </div>
    </div>
  </section>
</div>

<footer class="site-footer">
  <div class="footer-cols">
    <div class="footer-col" style="left:95px"><h5>Products</h5><ul><li>Alto Sax</li><li>Trumpet</li><li>Flute</li><li>Clarinet</li><li>Trombone</li></ul></div>
    <div class="footer-col" style="left:186px;top:44px"><ul><li>Tenor Sax</li><li>Baritone</li></ul></div>
    <div class="footer-col" style="left:351px"><h5>Additional Info</h5><ul><li>Tech Support</li><li>Learning Center</li><li>Shopping Cart</li><li>Instuments</li><li>Affiliate Program</li></ul></div>
    <div class="footer-col" style="left:483px;top:44px"><ul><li>Reseller Program</li><li>Privacy Policy</li><li>Terms of Use</li><li>Sitemap</li></ul></div>
    <div class="footer-col" style="left:649px"><h5>About Us</h5><ul><li>About Us</li><li>Careers</li><li>Blog</li><li>Press</li><li>Online Shopping</li></ul></div>
    <div class="footer-col" style="left:824px"><h5>Follow Us</h5><ul class="social"><li><span class="social-dot"></span>Friendline</li><li><span class="social-dot"></span>Chirpwire</li><li><span class="social-dot"></span>ClipCast</li></ul></div>
  </div>
  <div class="footer-bar">&copy; 2014 RidgeHornSupply.com. All Right Reserved</div>
</footer>
</body>
</html>
```